Invitation Design Project x 4 designs

4 of your designs that you submitted (1956036, 1956024, 1956019, 1956016) and would like each design to consist of a wedding invitation card, Save this date card, Seating cards, Table number cards and Thank you cards.

To give you an indication what each card should be for size and format please have a look at the link below and this should help give you a good understanding of what I am wanting...

http://www.plumvelle.co.nz/designs/off-the-rack/rustic/invitation

Industry/Entity Type

Wedding

```html
<!DOCTYPE html>
<html lang="en">
<head>
<meta charset="utf-8">
<title>Emily and Lucas – Wedding Card</title>
<link href="https://fonts.googleapis.com/css2?family=Italianno&family=Source+Sans+3:wght@600&display=swap" rel="stylesheet">
<style>
  :root {
    --mint: #acd5b5;
    --mint-soft: #b9dcc0;
    --cream: #fefcf0;
    --taupe: #a89a78;
  }
  * { margin: 0; padding: 0; box-sizing: border-box; }
  html, body {
    width: 1200px;
    height: 863px;
    overflow: hidden;
    background: var(--cream);
  }
  .card {
    position: relative;
    width: 1200px;
    height: 863px;
    background: var(--cream);
  }
  .floral-field {
    position: absolute;
    left: 0;
    width: 100%;
    background: linear-gradient(180deg, var(--mint) 0%, var(--mint-soft) 50%, var(--mint) 100%);
  }
  .floral-field--top { top: 0; height: 274px; }
  .floral-field--bottom { top: 690px; height: 173px; }

  .name-band {
    position: absolute;
    top: 274px;
    left: 0;
    width: 100%;
    height: 416px;
    background: var(--cream);
  }
  .rule {
    position: absolute;
    left: 0;
    width: 100%;
    height: 8px;
    background: var(--taupe);
  }
  .rule--top { top: 0; }
  .rule--bottom { bottom: 0; }
  .dot-row {
    position: absolute;
    left: 0;
    width: 100%;
    height: 8px;
    background: radial-gradient(circle, var(--taupe) 3px, transparent 3.6px) 4px 0 / 13.8px 8px repeat-x;
  }
  .dot-row--top { top: 15px; }
  .dot-row--bottom { bottom: 15px; }

  .couple-names {
    position: absolute;
    left: 0;
    top: 150px;
    width: 100%;
    display: flex;
    align-items: baseline;
    justify-content: center;
    gap: 30px;
    white-space: nowrap;
    font-weight: normal;
  }
  .couple-names__name {
    font-family: "Italianno", cursive;
    font-size: 150px;
    color: var(--taupe);
    line-height: 1;
  }
  .couple-names__join {
    font-family: "Source Sans 3", sans-serif;
    font-weight: 600;
    font-size: 122px;
    letter-spacing: 2px;
    color: var(--mint);
    line-height: 1;
  }
</style>
</head>
<body>
  <div class="card">
    <div class="floral-field floral-field--top" role="img" aria-label="Cream leaf and blossom pattern on mint green"></div>

    <section class="name-band">
      <div class="rule rule--top"></div>
      <div class="dot-row dot-row--top"></div>
      <h1 class="couple-names">
        <span class="couple-names__name">Emily</span>
        <span class="couple-names__join">and</span>
        <span class="couple-names__name">Lucas</span>
      </h1>
      <div class="dot-row dot-row--bottom"></div>
      <div class="rule rule--bottom"></div>
    </section>

    <div class="floral-field floral-field--bottom" role="img" aria-label="Cream leaf and blossom pattern on mint green"></div>
  </div>
</body>
</html>
```